Business Card Design

Company name is: Tallowmere Rescue Skills, LLC. We teach CPR/AED, First Aid, Bloodborne Pathogens and other health and safety classes. Looking for an eye-catching, progressive, cutting edge design.

Industry/Entity Type

Health

Contact Information for Business Card

Dale Fenwarick (555.218.4703)
Nora Quillstead (555.276.9148)
email is info@tallowmererescue.example
website is www.TallowmereRescue.example

```html
<!DOCTYPE html>
<html lang="en">
<head>
<meta charset="utf-8">
<title>Tallowmere Rescue Skills, LLC – Business Card</title>
<link rel="stylesheet" href="https://fonts.googleapis.com/css2?family=Source+Sans+3:wght@400;600&display=swap">
<style>
  :root {
    --card-bg: #ffffff;
    --brand-red: #e3101d;
    --ink: #111111;
    --edge: #9a9a9a;
    --shade-dark: #1f2021;
    --shade-mid: #5a5b5c;
    --shade-light: #b9babb;
  }
  html, body {
    margin: 0;
    padding: 0;
    overflow: hidden;
    background: var(--card-bg);
  }
  .card {
    position: relative;
    width: 1200px;
    height: 702px;
    background: var(--card-bg);
    overflow: hidden;
    font-family: "Source Sans 3", sans-serif;
  }
  .card__art {
    position: absolute;
    inset: 0;
    width: 1200px;
    height: 702px;
  }
  .company-name {
    position: absolute;
    left: 452px;
    top: 52px;
    margin: 0;
    font-family: "Source Sans 3", sans-serif;
    font-weight: 600;
    font-size: 62px;
    line-height: 104px;
    letter-spacing: 1px;
    color: var(--brand-red);
    text-transform: uppercase;
  }
  .company-name span { display: block; }
  .contacts {
    position: absolute;
    left: 0;
    width: 1164px;
    top: 338px;
    text-align: center;
    color: var(--ink);
    font-size: 47px;
    line-height: 52px;
  }
  .contacts p { margin: 0; }
  .contacts .web { font-size: 44px; margin-top: 2px; }
  .email {
    position: absolute;
    left: 0;
    width: 1164px;
    top: 608px;
    margin: 0;
    text-align: center;
    color: var(--ink);
    font-size: 42px;
    line-height: 48px;
  }
</style>
</head>
<body>
<div class="card">
  <svg class="card__art" viewBox="0 0 1200 702" aria-hidden="true">
    <defs>
      <linearGradient id="shade-top" x1="0" y1="0" x2="1" y2="1">
        <stop offset="0" stop-color="var(--shade-dark)"/>
        <stop offset="1" stop-color="var(--shade-mid)"/>
      </linearGradient>
      <linearGradient id="shade-bottom" x1="1" y1="1" x2="0" y2="0">
        <stop offset="0" stop-color="var(--shade-dark)"/>
        <stop offset="1" stop-color="var(--shade-mid)"/>
      </linearGradient>
    </defs>
    <!-- top-left facets -->
    <polygon class="facet facet--light" points="20,20 372,20 20,368" fill="var(--shade-light)"/>
    <polygon class="facet facet--mid" points="20,20 330,20 20,300" fill="var(--shade-mid)"/>
    <polygon class="facet facet--dark" points="20,20 270,20 20,240" fill="url(#shade-top)"/>
    <polygon class="facet facet--sheen" points="120,20 220,20 20,200 20,150" fill="#ffffff" opacity="0.12"/>
    <!-- bottom-right facets -->
    <polygon class="facet facet--light" points="1177,332 1177,680 822,680" fill="var(--shade-light)"/>
    <polygon class="facet facet--mid" points="1177,400 1177,680 880,680" fill="var(--shade-mid)"/>
    <polygon class="facet facet--dark" points="1177,470 1177,680 950,680" fill="url(#shade-bottom)"/>
    <polygon class="facet facet--sheen" points="1177,520 1177,570 1030,680 990,680" fill="#ffffff" opacity="0.12"/>
    <!-- card edge -->
    <polyline class="card-edge" points="1177,20 1177,680 20,680" fill="none" stroke="var(--edge)" stroke-width="1.5"/>
  </svg>

  <h1 class="company-name">
    <span>Tallowmere Rescue</span>
    <span>Skills, LLC</span>
  </h1>

  <div class="contacts">
    <p class="contact">Dale Fenwarick - 555.218.4703</p>
    <p class="contact">Nora Quillstead - 555.276.9148</p>
    <p class="web">www.TallowmereRescue.example</p>
  </div>

  <p class="email">info@tallowmererescue.example</p>
</div>
</body>
</html>
```